Grivo like IOS/Android app for Okinawa Island - TavuScout

TavuScout is the name of the app
The closest thing that I can relate this app to is a region specific Grivo app. The app is for the island of Okinawa and is geared towards English speaking travelers. The style of app that I prefer is a look and feel similar to that of the new Lodgemere app, color should also be similar if not the same as the lodgemere app.

The app needs to have the following screens

LOGIN SCREEN
1. App login page with a login for chatterly button or create an account option. Personally I would like an image in the background with a real beachy feel, but don't do this if it messes with your design.

2. Depending on the choice of login there will need to be a second login screen to create the account. Lodgemere does this nicely.

PRIMARY HOME
primary page similar to the primary layout when you get into the lodgemere app.
This page is kind of like the home page of the app and should include the following items:
search field
upcoming events
popular things to do
featured restaurants
Featured Places to stay
area guides
Moving here
(this will allow the person to select, housing agencies, auto dealers, schools etc) These are essentially just quick searches.
Each selection should be listed so that the user can swipe to the left or right in order to view more listings under the categories listed above. It will not be the full list but rather a sample.

SIDEBAR POPOUT MENU
Popout sidebar that contains the following selections
Places to Eat
Things to do
Attractions
Beaches
Shop
Farmers Markets
Places to Stay
Schools & DayCare
Housing
Auto
Events
Account settings
Add a business

LIST VIEW
4. List view page for whatever category the user selected. This will show all the listings for the specific category: The top should also have the featured listings for that category

INDIVIDUAL LISTING
5. Listing page
This will include photos, description, hours, map(this can be a button to view the map or the map), Reviews with a leave a review option

AREA GUIDES
6. Area Guides. This is where the user will be able to select a specific area and learn about it. It should include an area where there can be a description, photos with a hero photo image, a map, popular local attractions or things to do, best restaurants in the area, places to stay etc.

PROFILE PAGE
7. Profile page for the user where they can make any updates they need to

Every page but the listing page should include the search bar. When the user clicks in it they should be able to see a drop down of quick select searches or run a regular search.

Logo
I have attached a logo that was made that needs a redesign. The map marker contains the logo for Okinawa within it so it does need to be similar.

If you have any questions or need clarification please send me a message. I will respond promptly.
Thank you,

```html
<!DOCTYPE html>
<html lang="en">
<head>
<meta charset="utf-8">
<title>TavuScout – App Screens</title>
<link href="https://fonts.googleapis.com/css2?family=Mulish:wght@400;600;700;800&display=swap" rel="stylesheet">
<style>
:root{
  --accent:#e8505b;
  --accent-soft:#f3a9ae;
  --ink:#1f2229;
  --muted:#7d8189;
  --line:#e9eaee;
  --canvas:#dde3ea;
  --white:#ffffff;
}
*{box-sizing:border-box;margin:0;padding:0}
html,body{width:1200px;height:1166px;overflow:hidden;background:var(--canvas);font-family:"Mulish",sans-serif;color:var(--ink)}
.board{position:relative;width:1200px;height:1166px}
.brand{position:absolute;top:68px;left:0;width:1200px;display:flex;justify-content:center;align-items:center;gap:16px}
.brand-dot{width:56px;height:56px;border-radius:50%;background:var(--accent)}
.brand-name{font-size:38px;font-weight:400;letter-spacing:.5px;color:var(--ink)}
.screen{position:absolute;width:250px;background:var(--white);overflow:hidden;box-shadow:0 2px 10px rgba(40,50,70,.12)}
.status{height:16px;display:flex;justify-content:space-between;align-items:center;padding:0 5px;font-size:7px;font-weight:600}
.navbar{height:26px;display:flex;align-items:center;justify-content:center;position:relative;font-size:10.5px;font-weight:700;border-bottom:1px solid var(--accent-soft)}
.navbar .left{position:absolute;left:10px;top:8px}
.navbar .right{position:absolute;right:9px;top:7px;font-size:8.5px;color:var(--accent);font-weight:600}
.mini-brand{display:flex;align-items:center;gap:5px;font-weight:600;font-size:10.5px}
.mini-dot{width:13px;height:13px;border-radius:50%;background:var(--accent)}
.search{height:30px;display:flex;align-items:center;gap:6px;padding:0 12px;font-size:7.5px;color:#a9acb2;border-bottom:1px solid var(--line)}
.photo{position:absolute;border-radius:2px;overflow:hidden}
.photo span{position:absolute;left:0;right:0;bottom:8px;text-align:center;color:#fff;font-weight:700;font-size:7px}
.h-section{position:absolute;left:12px;font-size:14px;font-weight:600;color:var(--accent)}
.h-sub{position:absolute;left:12px;font-size:8.5px;font-weight:700}
/* login */
.login{background:linear-gradient(180deg,#2e2f3f 0%,#3d3a4c 35%,#4a3c4b 55%,#3a3546 75%,#2d3040 100%);color:#fff}
.login .status{color:#fff}
.btn-fb{position:absolute;left:20px;width:210px;top:221px;height:36px;border-radius:18px;background:var(--accent);display:flex;align-items:center;justify-content:center;gap:8px;font-size:10.5px;font-weight:700}
.btn-ghost{position:absolute;left:20px;width:210px;top:266px;height:36px;border-radius:18px;border:1.5px solid #fff;display:flex;align-items:center;justify-content:center;font-size:10.5px;font-weight:600}
/* list */
.row{position:absolute;left:0;width:250px;height:83px}
.row .thumb{position:absolute;left:12px;top:0;width:70px;height:70px}
.row .jp{position:absolute;left:92px;top:1px;font-size:7px;color:#444}
.row .title{position:absolute;left:92px;top:12px;width:150px;font-size:13px;font-weight:600;line-height:1.2}
.row .town{font-size:8.5px;color:var(--accent);display:flex;align-items:center;gap:4px;margin-top:4px;font-weight:400}
.row::after{content:"";position:absolute;left:92px;right:12px;bottom:5px;height:1px;background:var(--line)}
/* menu */
.menu-panel{position:absolute;left:0;top:0;width:200px;height:444px;background:#fff;border-right:1px solid var(--line)}
.menu-item{position:absolute;left:14px;display:flex;align-items:center;gap:12px;font-size:8.8px;letter-spacing:.9px}
.menu-item svg{width:16px;height:16px}
/* account */
.field{position:absolute;left:12px;right:12px;height:27px;display:flex;align-items:center;font-size:8.5px;border-bottom:1px solid var(--line)}
.field .label{width:82px;display:flex;align-items:center;gap:6px;font-weight:600}
.field .value{color:#555}
.outline-btn{position:absolute;border:1px solid var(--accent);border-radius:13px;height:25px;display:flex;align-items:center;justify-content:center;gap:6px;color:var(--accent);font-size:9px}
/* listing */
.lbl{position:absolute;font-size:10.5px;color:var(--accent);font-weight:600}
.body-text{position:absolute;font-size:7.4px;color:#666;line-height:1.5}
.review-name{font-size:9.5px;color:var(--accent)}
.stars{color:#f5a623;font-size:7px;letter-spacing:.5px}
.stars .off{color:#d8d8d8}
</style>
</head>
<body>
<div class="board">

  <div class="brand">
    <div class="brand-dot"></div>
    <div class="brand-name">TavuScout</div>
  </div>

  <!-- Login -->
  <section class="screen login" style="left:70px;top:170px;height:444px" role="img" aria-label="Login screen over a dusk beach photo">
    <div class="status"><span>●●●○○ Carrier</span><span>4:21 PM</span><span>100% ▬</span></div>
    <div style="position:absolute;right:22px;top:44px;font-size:11px;font-weight:600">Log in</div>
    <div style="position:absolute;left:48px;top:112px;display:flex;align-items:center;gap:10px">
      <div style="width:38px;height:38px;border-radius:50%;background:var(--accent)"></div>
      <div>
        <div style="font-size:10.5px">Welcome to</div>
        <div style="font-size:22px;font-weight:600;color:var(--accent);line-height:1.1">TavuScout</div>
      </div>
    </div>
    <div class="btn-fb"><span style="width:10px;height:10px;background:#fff;display:inline-block"></span>Continue with Chatterly</div>
    <div class="btn-ghost">Create an Account</div>
    <div style="position:absolute;top:346px;width:100%;text-align:center;font-size:10.5px;font-weight:600">More Options</div>
  </section>

  <!-- Side menu -->
  <section class="screen" style="left:70px;top:634px;height:444px">
    <div style="position:absolute;left:200px;top:0;width:50px;height:444px;background:#fff">
      <svg style="position:absolute;left:12px;top:30px" width="12" height="10"><path d="M0 1h12M0 5h12M0 9h12" stroke="#e8505b" stroke-width="1"/></svg>
      <div style="position:absolute;left:0;top:50px;width:50px;height:1px;background:var(--line)"></div>
      <div style="position:absolute;left:12px;top:57px;font-size:7.5px;color:#aaa;white-space:nowrap">⌕ Searc</div>
      <div style="position:absolute;left:11px;top:87px;font-size:14px;color:var(--accent);font-weight:600">Upco</div>
      <div role="img" aria-label="Festival dancers photo" style="position:absolute;left:12px;top:115px;width:40px;height:93px;background:linear-gradient(160deg,#4a5a8a,#b84a4a 60%,#222)"></div>
      <div style="position:absolute;left:11px;top:231px;font-size:14px;color:var(--accent);font-weight:600">Popu</div>
      <div role="img" aria-label="Children playing photo" style="position:absolute;left:12px;top:258px;width:40px;height:93px;background:linear-gradient(160deg,#c8a820,#6b5a10 70%,#2a2a2a)"></div>
      <div style="position:absolute;left:11px;top:375px;font-size:14px;color:var(--accent);font-weight:600">Featu</div>
      <div style="position:absolute;left:12px;top:402px;font-size:8.5px;font-weight:700">Restaura</div>
      <div role="img" aria-label="Restaurant dish photo" style="position:absolute;left:12px;top:418px;width:40px;height:30px;background:linear-gradient(160deg,#777,#333)"></div>
    </div>
    <div class="menu-panel">
      <div style="position:absolute;left:10px;top:13px;display:flex;align-items:center;gap:6px">
        <div style="width:19px;height:19px;border-radius:50%;background:var(--accent)"></div>
        <span style="font-size:13px;color:var(--accent);font-weight:600">TavuScout</span>
      </div>
      <div style="position:absolute;left:132px;top:12px;height:20px;border-left:1px solid var(--line)"></div>
      <div style="position:absolute;right:12px;top:18px;font-size:8.5px;color:var(--accent)">⚙ Settings</div>
      <div style="position:absolute;left:0;top:42px;width:200px;height:1.5px;background:var(--accent)"></div>

      <div class="menu-item" style="top:59px"><svg viewBox="0 0 16 16" fill="none" stroke="#e8505b"><path d="M3 1v14M1 1v4h4V1M10 1h4v7h-4zM12 8v7"/></svg>PLACES TO EAT</div>
      <div class="menu-item" style="top:92px"><svg viewBox="0 0 16 16" fill="none" stroke="#e8505b"><circle cx="7" cy="8" r="5"/><circle cx="7" cy="8" r="2"/><path d="M9 8h6"/></svg>THINGS TO DO</div>
      <div class="menu-item" style="top:125px"><svg viewBox="0 0 16 16" fill="none" stroke="#e8505b"><path d="M8 15s5-5 5-9a5 5 0 0 0-10 0c0 4 5 9 5 9z"/><circle cx="8" cy="6" r="2"/></svg>ATTRACTIONS</div>
      <div class="menu-item" style="top:158px"><svg viewBox="0 0 16 16" fill="none" stroke="#e8505b"><path d="M2 7a7 7 0 0 1 12 0zM8 7l3 8M1 15h14"/></svg>BEACHES</div>
      <div class="menu-item" style="top:191px"><svg viewBox="0 0 16 16" fill="none" stroke="#e8505b"><path d="M1 2h2l2 9h8l2-6H4"/><circle cx="6" cy="14" r="1"/><circle cx="12" cy="14" r="1"/></svg>SHOP</div>
      <div class="menu-item" style="top:224px"><svg viewBox="0 0 16 16" fill="none" stroke="#e8505b"><path d="M1 3v12M5 3v12M11 3v12M15 3v12M1 7h14M1 11h14"/></svg>FARMERS MARKETS</div>
      <div class="menu-item" style="top:257px"><svg viewBox="0 0 16 16" fill="none" stroke="#e8505b"><path d="M1 13V5h14v8M1 10h14M3 5V3h10v2"/></svg>PLACES TO STAY</div>
      <div class="menu-item" style="top:290px"><svg viewBox="0 0 16 16" fill="none" stroke="#e8505b"><path d="M1 14h14M2 14V6h12v8M4 6l4-4 4 4"/></svg>SCHOOLS &amp; DAYCARE</div>
      <div class="menu-item" style="top:323px"><svg viewBox="0 0 16 16" fill="none" stroke="#e8505b"><path d="M2 8l6-6 6 6M3 7v8h10V7M7 15v-4h2v4"/></svg>HOUSING</div>
      <div class="menu-item" style="top:356px"><svg viewBox="0 0 16 16" fill="none" stroke="#e8505b"><path d="M1 11V8l2-4h10l2 4v3zM3 11v3M13 11v3"/></svg>AUTO</div>
      <div class="menu-item" style="top:389px"><svg viewBox="0 0 16 16" fill="none" stroke="#e8505b"><rect x="1" y="3" width="14" height="12"/><path d="M1 6h14M5 1v3M11 1v3"/></svg>EVENTS</div>
      <div class="menu-item" style="top:422px"><svg viewBox="0 0 16 16" fill="none" stroke="#e8505b"><rect x="1" y="5" width="14" height="10"/><path d="M5 5V2h6v3M1 9h14"/></svg>ADD A BUSINESS</div>
    </div>
  </section>

  <!-- Home -->
  <section class="screen" style="left:340px;top:170px;height:908px">
    <div class="status"><span>●●●○○ Carrier</span><span>4:21 PM</span><span>100% ▬</span></div>
    <div class="navbar" style="border-bottom-color:var(--line)">
      <svg class="left" width="12" height="10"><path d="M0 1h12M0 5h12M0 9h12" stroke="#e8505b" stroke-width="1"/></svg>
      <div class="mini-brand"><span class="mini-dot"></span>TavuScout</div>
    </div>
    <div class="search"><svg width="9" height="9" viewBox="0 0 9 9" fill="none" stroke="#aaa"><circle cx="3.8" cy="3.8" r="3"/><path d="M6 6l2.5 2.5"/></svg>Search for locations or events</div>

    <div class="h-section" style="top:86px">Upcoming events</div>
    <div class="photo" role="img" aria-label="Festival drum dancers at night" style="left:12px;top:114px;width:226px;height:93px;background:linear-gradient(160deg,#2f3c6d,#b1454a 55%,#1f1f27)">
      <span style="bottom:22px;font-size:10px">Eisa Festival 2016</span>
      <span style="bottom:12px;font-size:6.5px;color:var(--accent-soft);font-weight:600">Sep 4, 2016</span>
    </div>
    <div class="photo" style="left:244px;top:114px;width:10px;height:93px;background:#3b3f57"></div>

    <div class="h-section" style="top:229px">Popular things to do</div>
    <div class="photo" role="img" aria-label="Children at a summer camp" style="left:12px;top:257px;width:226px;height:93px;background:linear-gradient(160deg,#d6b81e,#8c7a16 55%,#262626)">
      <span style="bottom:12px;font-size:10px">Summer Adventure School</span>
    </div>
    <div class="photo" style="left:244px;top:257px;width:10px;height:93px;background:#2c2c2c"></div>

    <div class="h-section" style="top:372px">Featured</div>
    <div class="h-sub" style="top:400px">Restaurants</div>
    <div class="photo" role="img" aria-label="Grilled meat dishes" style="left:12px;top:417px;width:80px;height:73px;background:linear-gradient(160deg,#9a9a98,#4a4844)"><span>Yakiniku<br>Sora</span></div>
    <div class="photo" role="img" aria-label="Japanese set meal" style="left:99px;top:417px;width:80px;height:73px;background:linear-gradient(160deg,#c0632f,#6a2e1a)"><span>Minato<br>Japanese Restaur…</span></div>
    <div class="photo" role="img" aria-label="Tavern interior with lanterns" style="left:186px;top:417px;width:80px;height:73px;background:linear-gradient(160deg,#6b5a44,#1f1a16)"><span style="text-align:left;left:14px">Ginza Tave</span></div>

    <div class="h-sub" style="top:505px">Places to stay</div>
    <div class="photo" role="img" aria-label="Hotel lobby" style="left:12px;top:522px;width:80px;height:74px;background:linear-gradient(160deg,#8e7d6a,#2d2622)"><span>Estella Hotel</span></div>
    <div class="photo" role="img" aria-label="Palm trees by a beach hotel" style="left:99px;top:522px;width:80px;height:74px;background:linear-gradient(160deg,#3d6e86,#2d4a30)"><span>Hotel Shell Beach</span></div>
    <div class="photo" role="img" aria-label="Terrace resort pool" style="left:186px;top:522px;width:80px;height:74px;background:linear-gradient(160deg,#3c6aa8,#2a3b45)"><span style="text-align:left;left:6px">Aza Terrace Bea</span></div>

    <div class="h-section" style="top:618px">Area Guides</div>
    <div class="photo" role="img" aria-label="Coastal town street" style="left:12px;top:645px;width:80px;height:73px;background:linear-gradient(160deg,#6a98b8,#7c7060)"><span>Central Area</span></div>
    <div class="photo" role="img" aria-label="Forested hills" style="left:99px;top:645px;width:80px;height:73px;background:linear-gradient(160deg,#6f8a6a,#2f4a2c)"><span>Northern Area</span></div>
    <div class="photo" role="img" aria-label="City street with trees" style="left:186px;top:645px;width:80px;height:73px;background:linear-gradient(160deg,#5d7a4e,#3c3c40)"><span style="text-align:left;left:22px">Naha City</span></div>

    <div class="h-section" style="top:743px">Moving Here</div>
    <div class="photo" role="img" aria-label="Car lot" style="left:12px;top:770px;width:71px;height:46px;background:#4a5a78"><span style="bottom:16px">Auto Dealers</span></div>
    <div class="photo" role="img" aria-label="Apartment blocks" style="left:89px;top:770px;width:71px;height:46px;background:#5e6670"><span style="bottom:12px">Housing<br>Agencies</span></div>
    <div class="photo" role="img" aria-label="Clinic" style="left:167px;top:770px;width:71px;height:46px;background:#4d5a70"><span style="bottom:16px">Healthcare</span></div>
    <div class="photo" role="img" aria-label="School building" style="left:12px;top:823px;width:71px;height:47px;background:#4a5670"><span style="bottom:16px">Schools</span></div>
    <div class="photo" role="img" aria-label="Shop aisle" style="left:89px;top:823px;width:71px;height:47px;background:#55627a"><span style="bottom:16px">Shop</span></div>
    <div class="photo" role="img" aria-label="Office workers" style="left:167px;top:823px;width:71px;height:47px;background:#4c5a74"><span style="bottom:16px">To Work</span></div>
  </section>

  <!-- Attractions list -->
  <section class="screen" style="left:610px;top:170px;height:444px">
    <div class="status"><span>●●●○○ Carrier</span><span>4:21 PM</span><span>100% ▬</span></div>
    <div class="navbar">
      <svg class="left" width="12" height="10"><path d="M12 5H1M5 1L1 5l4 4" stroke="#e8505b" fill="none"/></svg>
      Attractions
    </div>
    <div class="row" style="top:55px">
      <div class="thumb photo" role="img" aria-label="Paddleboarder at sunset" style="background:linear-gradient(180deg,#56627a,#d8a25a 55%,#3a3024)"></div>
      <div class="jp">リーフサップ</div>
      <div class="title">Reef-SUP takes you places<div class="town">◉ Kadena Town</div></div>
    </div>
    <div class="row" style="top:138px">
      <div class="thumb photo" role="img" aria-label="Aquarium tank with whale shark" style="background:linear-gradient(180deg,#3a7fa8,#17405a 75%,#0c1820)"></div>
      <div class="jp">青潮公園</div>
      <div class="title">Blue Tide Park<div class="town">◉ Motobu Town</div></div>
    </div>
    <div class="row" style="top:221px">
      <div class="thumb photo" role="img" aria-label="Farm with water buffalo" style="background:linear-gradient(180deg,#6e8c60,#7a6a52)"></div>
      <div class="jp">きよらファーム</div>
      <div class="title">Kiyora Farm<div class="town">◉ Itoman City</div></div>
    </div>
    <div class="row" style="top:304px">
      <div class="thumb photo" role="img" aria-label="Planetarium starry sky" style="background:linear-gradient(180deg,#2a3030,#0f1414)"></div>
      <div class="jp">海辺文化館</div>
      <div class="title">Seaside Culture Museum<div class="town">◉ Motobu-cho</div></div>
    </div>
    <div class="row" style="top:387px">
      <div class="thumb photo" role="img" aria-label="Lit ship in port at night" style="background:linear-gradient(180deg,#3a3220,#b88a2e 60%,#1a1510)"></div>
      <div class="jp">港桟橋</div>
      <div class="title">Minato Pier<div class="town">◉ Naha City</div></div>
    </div>
  </section>

  <!-- Account settings -->
  <section class="screen" style="left:610px;top:634px;height:444px">
    <div class="status"><span>●●●○○ Carrier</span><span>4:21 PM</span><span>100% ▬</span></div>
    <div class="navbar">
      <svg class="left" width="12" height="10"><path d="M12 5H1M5 1L1 5l4 4" stroke="#e8505b" fill="none"/></svg>
      Account Settings
      <span class="right">Logout</span>
    </div>
    <div role="img" aria-label="User profile photo" style="position:absolute;left:84px;top:60px;width:82px;height:82px;border-radius:50%;background:linear-gradient(160deg,#8a9aa0,#4a4a48);border:2px solid #fff;box-shadow:0 0 0 1px var(--line)"></div>
    <div style="position:absolute;top:152px;width:100%;text-align:center;font-size:13.5px;font-weight:600;color:var(--accent)">Owen Parrish</div>
    <div style="position:absolute;left:0;top:185px;width:100%;height:1.5px;background:var(--accent-soft)"></div>
    <div class="field" style="top:196px"><span class="label"><span style="color:var(--accent)">●</span>First Name</span><span class="value">Owen</span></div>
    <div class="field" style="top:223px"><span class="label"><span style="color:var(--accent)">●</span>Last Name</span><span class="value">Parrish</span></div>
    <div class="field" style="top:250px"><span class="label"><span style="color:var(--accent)">✉</span>Email</span><span class="value">user@email.com</span></div>
    <div class="outline-btn" style="left:77px;width:96px;top:311px">✎ Edit Profile</div>
    <div class="outline-btn" style="left:61px;width:129px;top:344px">🔒︎ Change Password</div>
  </section>

  <!-- Listing -->
  <section class="screen" style="left:880px;top:170px;height:659px">
    <div role="img" aria-label="Aquarium tank with whale shark and silhouetted visitors" style="position:absolute;left:0;top:0;width:250px;height:189px;background:linear-gradient(180deg,#0f2c3e,#2f7296 40%,#1a4a66 75%,#0a1419)"></div>
    <div class="status" style="position:relative;color:#fff;background:rgba(0,0,0,.25)"><span>●●●○○ Carrier</span><span>4:21 PM</span><span>100% ▬</span></div>
    <div style="position:relative;height:26px;display:flex;align-items:center;justify-content:center;color:#fff;font-size:10.5px;font-weight:700">
      <svg style="position:absolute;left:12px;top:8px" width="12" height="10"><path d="M12 5H1M5 1L1 5l4 4" stroke="#fff" fill="none"/></svg>
      Blue Tide Park
    </div>
    <div style="position:absolute;left:12px;top:128px;color:#fff">
      <div style="font-size:7.5px;font-weight:600">青潮公園</div>
      <div style="font-size:14px;font-weight:700">Blue Tide Park</div>
      <div style="font-size:9px;font-weight:600;margin-top:2px">◉ Motobu Town</div>
    </div>
    <div style="position:absolute;left:198px;top:170px;width:40px;height:40px;border-radius:50%;background:#fff;box-shadow:0 2px 6px rgba(0,0,0,.2);display:flex;align-items:center;justify-content:center">
      <svg width="20" height="18" viewBox="0 0 20 18"><path d="M10 16S2 11 2 5.5A4 4 0 0 1 10 4a4 4 0 0 1 8 1.5C18 11 10 16 10 16z" fill="none" stroke="#e8505b" stroke-width="1.6"/></svg>
    </div>
    <div class="lbl" style="left:12px;top:205px">Description</div>
    <div class="body-text" style="left:12px;top:222px;width:228px">Internationally renowned for huge whale sharks measuring 8.6 meters in length and various other species of fish that can be observed through a massive acrylic panel, the Kaiyo Reef Aquarium is a must-see when visiting Okinawa.</div>
    <div style="position:absolute;left:0;top:289px;width:250px;height:1px;background:var(--line)"></div>
    <div style="position:absolute;left:125px;top:289px;width:1px;height:60px;background:var(--line)"></div>
    <div class="lbl" style="left:12px;top:297px">Address</div>
    <div class="body-text" style="left:12px;top:315px;width:105px">118 Kise, Motobu Town, Okinawa</div>
    <div class="lbl" style="left:133px;top:297px">Hours</div>
    <div class="body-text" style="left:133px;top:315px">Oct-Feb: 8:30-18:30<br>Mar-Sep: 8:30-20:00</div>
    <div role="img" aria-label="Street map of the park area with a location pin" style="position:absolute;left:0;top:349px;width:250px;height:67px;background:linear-gradient(90deg,#bfe0a8 0%,#bfe0a8 35%,#f2ece2 36%,#f2ece2 100%)"></div>
    <div style="position:absolute;left:12px;top:434px;font-size:13px;font-weight:600">2 Reviews</div>
    <div class="stars" style="position:absolute;left:12px;top:452px;font-size:9px">★★★★<span class="off">★</span></div>
    <div class="outline-btn" style="left:157px;width:82px;height:20px;top:441px;font-size:7.5px;border-radius:10px">Write a Review</div>

    <div role="img" aria-label="Reviewer avatar" style="position:absolute;left:12px;top:480px;width:28px;height:28px;border-radius:50%;background:#b8a48a"></div>
    <div style="position:absolute;left:45px;top:481px"><span class="review-name">Dale Hurst</span> <span class="stars">★★★★★</span><div style="font-size:7px;color:#555;margin-top:2px">Feb 01, 2016</div></div>
    <div class="body-text" style="left:12px;top:513px;width:226px">We had a great time every time we went while being stationed in Okinawa Japan. We love this place it was awesome and my kids enjoy it too.</div>
    <div style="position:absolute;left:12px;right:12px;top:552px;height:1px;background:var(--line)"></div>

    <div role="img" aria-label="Reviewer avatar" style="position:absolute;left:12px;top:562px;width:28px;height:28px;border-radius:50%;background:#c9b08a"></div>
    <div style="position:absolute;left:45px;top:563px"><span class="review-name">Mina Clore</span> <span class="stars">★★★<span class="off">★★</span></span><div style="font-size:7px;color:#555;margin-top:2px">Jan 25, 2016</div></div>
    <div class="body-text" style="left:12px;top:596px;width:226px">We had a great time every time we went while being stationed in Okinawa Japan. We love this place it was awesome and my kids enjoy it too.</div>
    <div style="position:absolute;left:12px;right:12px;top:635px;height:1px;background:var(--line)"></div>
  </section>

</div>
</body>
</html>
```